ParcelLantern shopping service flyer

We are a Korean shopping service. The attached picture explains our service. We would like to create a postcard or slightly larger sized flyer advertising our service. Front side will be graphics and back side text. For the front side, we want an updated version of the attached picture with our new logo and colours. And for the back side, create a simple design on the back side which we can enter all the text. Need font and design options.

Target Market(s)

20s and 30s females shopping for clothing (people not in Korea), shoppers are not Korean.

Industry/Entity Type

Online Shopping

Requirements
Must have
• For the front side, we want an updated version of the attached picture with our new logo and colours. And for the back side, create a simple design on the back side which we can enter all the text. Need font and design options.
Nice to have
• Little to no text on the front side.

```html
<!DOCTYPE html>
<html lang="en">
<head>
<meta charset="utf-8">
<title>ParcelLantern flyer</title>
<link href="https://fonts.googleapis.com/css2?family=Bebas+Neue&family=Open+Sans:wght@400;600;700;800&display=swap" rel="stylesheet">
<style>
:root{
  --teal:#1f9e8e;
  --teal-soft:#56bfb0;
  --teal-line:#4fb8a9;
  --orange:#e8774f;
  --paper:#f2f2f2;
  --white:#ffffff;
  --ink:#1c1c1c;
  --stage:#e4e4e4;
}
*{margin:0;padding:0;box-sizing:border-box}
html,body{width:966px;height:1200px;overflow:hidden;background:var(--stage)}
body{position:relative;font-family:"Open Sans",Arial,sans-serif;color:var(--ink)}
.card{position:absolute;left:93px;width:780px;height:555px;overflow:hidden;background:var(--paper);box-shadow:0 6px 18px rgba(0,0,0,.25)}
.card--front{top:40px}
.card--back{top:620px;background:var(--white)}
.card__bg{position:absolute;inset:0;width:780px;height:555px}
.abs{position:absolute}
.illustration{position:absolute;border-radius:8px}
.pill{position:absolute;height:20px;border-radius:10px;background:var(--teal-soft);color:var(--white);font-size:12px;font-weight:600;text-align:center;line-height:20px}
.wordmark{position:absolute;font-weight:800;line-height:.95;text-align:center;letter-spacing:-1px}
.url-tag{position:absolute;height:30px;color:var(--white);font-weight:700;font-size:19px;letter-spacing:1px;display:flex;align-items:center;justify-content:center;gap:8px}
.url-tag::before{content:"";position:absolute;inset:0;background:var(--orange);transform:skewX(-14deg);z-index:0}
.url-tag span{position:relative;z-index:1}
.url-tag .dot{width:12px;height:12px;border-radius:50%;background:var(--white)}
.step{position:absolute;width:150px;text-align:center}
.step__ring{position:absolute;left:11px;top:0;width:128px;height:128px}
.step__art{position:absolute;left:35px;top:30px;width:80px;height:80px;border-radius:8px}
.step__label{position:absolute;top:137px;width:150px;font-size:12.5px;line-height:20px;text-transform:uppercase}
.headline{position:absolute;left:27px;top:166px;font-family:"Bebas Neue",Impact,sans-serif;font-size:49px;line-height:1;color:var(--ink)}
.subhead{position:absolute;left:27px;top:226px;font-size:20px;font-weight:600;text-transform:uppercase;letter-spacing:-.3px}
.tagline{position:absolute;left:236px;top:50px;width:300px;text-align:center;color:var(--orange);font-weight:700;font-size:16.5px;line-height:24px;text-transform:uppercase}
.provide-tag{position:absolute;left:27px;top:291px;width:252px;height:28px;color:var(--white);font-size:19px;letter-spacing:2px;font-weight:600;padding-left:14px;line-height:28px}
.provide-tag::before{content:"";position:absolute;inset:0;background:var(--orange);transform:skewX(-14deg);z-index:0}
.provide-tag span{position:relative}
.benefits{position:absolute;left:29px;top:333px;list-style:none}
.benefits li{display:flex;align-items:center;gap:12px;height:37px;color:var(--white);font-size:17px;font-weight:600;text-transform:uppercase;letter-spacing:-.2px}
.tick{width:22px;height:22px;border-radius:3px;background:var(--orange);flex:none}
.follow{position:absolute;left:29px;top:452px;font-size:13px;font-weight:600;text-transform:uppercase;color:var(--ink);display:flex;align-items:center;gap:5px;white-space:nowrap;letter-spacing:-.2px}
.follow .handle{color:var(--orange)}
.follow .sq{width:13px;height:13px;border-radius:3px;background:var(--orange)}
.footnote{position:absolute;left:0;width:780px;top:530px;text-align:center;color:var(--white);font-size:10px;font-weight:600}
</style>
</head>
<body>

<section class="card card--front" aria-label="Flyer front">
  <svg class="card__bg" viewBox="0 0 780 555" aria-hidden="true">
    <rect width="780" height="555" fill="#f0f0f0"/>
    <path d="M0 0H780V285Q390 430 0 285Z" fill="#e9e9e9"/>
    <path d="M0 0H780V278Q390 418 0 272Z" fill="#1f9e8e"/>
    <rect x="130" y="40" width="90" height="230" fill="#ffffff" opacity=".06"/>
    <rect x="250" y="20" width="60" height="260" fill="#ffffff" opacity=".05"/>
    <rect x="480" y="60" width="70" height="220" fill="#ffffff" opacity=".05"/>
    <path d="M160 470 Q180 480 205 472" fill="none" stroke="#9aa" stroke-width="1" stroke-dasharray="2 3"/>
    <path d="M368 378 Q390 368 415 372" fill="none" stroke="#9aa" stroke-width="1" stroke-dasharray="2 3"/>
    <path d="M555 470 Q575 480 600 472" fill="none" stroke="#9aa" stroke-width="1" stroke-dasharray="2 3"/>
  </svg>

  <div class="illustration" role="img" aria-label="Customer illustration" style="left:92px;top:122px;width:84px;height:94px;background:rgba(255,255,255,.85);border-radius:40px 40px 12px 12px"></div>
  <div class="pill" style="left:71px;top:236px;width:120px">CUSTOMER</div>

  <div class="wordmark" style="left:230px;top:78px;width:300px;font-size:52px;color:var(--white)">Parcel<br>Lantern</div>

  <div class="illustration" role="img" aria-label="Online shop storefront screens illustration" style="left:537px;top:111px;width:200px;height:94px;background:linear-gradient(180deg,#f4a88c 0 22%,#3fb0a0 22% 80%,#d9d9d9 80%)"></div>
  <div class="pill" style="left:574px;top:236px;width:122px">ONLINE SHOPS</div>

  <div class="url-tag" style="left:244px;top:292px;width:300px"><span class="dot"></span><span>parcellantern.com</span></div>

  <div class="step" style="left:35px;top:358px">
    <svg class="step__ring" viewBox="0 0 128 128" aria-hidden="true"><path d="M14 92A56 56 0 1 1 112 92" fill="none" stroke="var(--teal-line)" stroke-width="2.5"/></svg>
    <div class="step__art" role="img" aria-label="Phone with pay now receipt illustration" style="background:linear-gradient(180deg,#eee,#3fa7c9)"></div>
    <div class="step__label">Request &amp;<br>Payment</div>
  </div>
  <div class="step" style="left:218px;top:358px">
    <svg class="step__ring" viewBox="0 0 128 128" aria-hidden="true"><path d="M14 92A56 56 0 1 1 112 92" fill="none" stroke="var(--teal-line)" stroke-width="2.5"/></svg>
    <div class="step__art" role="img" aria-label="Online shop screen illustration" style="background:linear-gradient(180deg,#f4a88c 0 25%,#3fb0a0 25% 80%,#d9d9d9 80%)"></div>
    <div class="step__label">Shopping</div>
  </div>
  <div class="step" style="left:412px;top:358px">
    <svg class="step__ring" viewBox="0 0 128 128" aria-hidden="true"><path d="M14 92A56 56 0 1 1 112 92" fill="none" stroke="var(--teal-line)" stroke-width="2.5"/></svg>
    <div class="step__art" role="img" aria-label="Shopping bags and boxes illustration" style="background:linear-gradient(135deg,#4fb8a9,#f0a58a)"></div>
    <div class="step__label">Receive &amp;<br>Consolidate</div>
  </div>
  <div class="step" style="left:606px;top:358px">
    <svg class="step__ring" viewBox="0 0 128 128" aria-hidden="true"><path d="M14 92A56 56 0 1 1 112 92" fill="none" stroke="var(--teal-line)" stroke-width="2.5"/></svg>
    <div class="step__art" role="img" aria-label="Delivery truck with parcels illustration" style="background:linear-gradient(180deg,#d9a865,#e8774f)"></div>
    <div class="step__label">Shipping<br>Worldwide</div>
  </div>
</section>

<section class="card card--back" aria-label="Flyer back">
  <svg class="card__bg" viewBox="0 0 780 555" aria-hidden="true">
    <rect width="780" height="555" fill="#ffffff"/>
    <path d="M500 0H780V170Q600 60 500 0Z" fill="#f2f2f2"/>
    <path d="M0 200Q200 320 780 160V555H0Z" fill="#e6f3f1"/>
    <path d="M0 255Q330 350 780 168V555H0Z" fill="#56bfb0"/>
  </svg>

  <div class="wordmark" style="left:40px;top:30px;width:180px;font-size:40px;color:var(--teal)">Parcel<br>Lantern</div>

  <p class="tagline">I not only make it easy,<br>it’s smart to shop with<br>ParcelLantern.</p>

  <div class="illustration" role="img" aria-label="Online shop screen illustration" style="left:574px;top:30px;width:160px;height:112px;background:linear-gradient(180deg,#f4a88c 0 22%,#3fb0a0 22% 75%,#dcdcdc 75%)"></div>

  <h1 class="headline">The Fastest Korean Shopping Service</h1>
  <p class="subhead">Get the hottest trending products first</p>

  <div class="provide-tag"><span>WE PROVIDE:</span></div>
  <ul class="benefits">
    <li><svg class="tick" viewBox="0 0 22 22" aria-hidden="true"><rect width="22" height="22" rx="3" fill="#e8774f"/><path d="M5 11.5l4 4 8-9" fill="none" stroke="#fff" stroke-width="2.6"/></svg>A quick turn around</li>
    <li><svg class="tick" viewBox="0 0 22 22" aria-hidden="true"><rect width="22" height="22" rx="3" fill="#e8774f"/><path d="M5 11.5l4 4 8-9" fill="none" stroke="#fff" stroke-width="2.6"/></svg>The fastest shipping options</li>
    <li><svg class="tick" viewBox="0 0 22 22" aria-hidden="true"><rect width="22" height="22" rx="3" fill="#e8774f"/><path d="M5 11.5l4 4 8-9" fill="none" stroke="#fff" stroke-width="2.6"/></svg>A guarantee you will get the items you request or your money back*</li>
  </ul>

  <p class="follow">Follow <span class="sq"></span><span class="handle">@parcellantern</span> on Snapfolio to see more unique items available from Korea!</p>

  <div class="url-tag" style="left:236px;top:491px;width:296px"><span class="dot"></span><span>parcellantern.com</span></div>
  <p class="footnote">*refunds are on a product by product basis.</p>
</section>

</body>
</html>
```